Redesign of iOS App Moriva Tutor

Redesign of existing App Moriva Tutor, an app that helps learning Japanese Kanjis, Hiragana, Katakana.

The functionallity should remain the same as today: the app is free, you may download it at the app store. But: I like the design of my other apps better ;)

Target Market(s)

Students learning Japanese

Industry/Entity Type

Teacher

Font styles to use
Sans Serif

Requirements
Must have
• Moriva Tutor has 7 main screens, all screens has to be designed for iPhone and iPad: Main, Settings, Reading Tests, Writing Tests, Game, Paper Mode, Search
Nice to have
• I like the logo as it is today

```html
<!DOCTYPE html>
<html lang="en">
<head>
<meta charset="utf-8">
<title>Moriva Tutor – Menu</title>
<link rel="stylesheet" href="https://fonts.googleapis.com/css2?family=Inter:wght@400;500;600&display=swap">
<style>
  :root {
    --page: #f2f3f5;
    --status-bg: #000000;
    --status-fg: #ffffff;
    --menu-bg: #a86b3c;
    --menu-line: #b9804f;
    --menu-text: #ffffff;
    --menu-btn: #c07d45;
    --menu-btn-edge: #96592c;
    --search-bg: #ffffff;
    --search-text: #6d6d6d;
    --wood-top: #b07a4a;
    --wood-main: #9e6a3e;
    --wood-edge: #8a5a32;
    --tile: #a77445;
    --tile-edge: #8d5f36;
    --tile-label: #d4b08c;
    --score: #7a9a3a;
    --card: #d3b59c;
    --card-line: #c5a68a;
    --next-bg: #d1b397;
    --next-text: #a86b3c;
  }
  * { margin: 0; padding: 0; box-sizing: border-box; }
  html, body {
    width: 1000px; height: 1200px; overflow: hidden;
    background: var(--page);
    font-family: "Inter", "Helvetica Neue", Arial, sans-serif;
  }
  .stage { position: relative; width: 1000px; height: 1200px; }
  .screen {
    position: absolute; left: 189px; top: 48px;
    width: 566px; height: 1004px;
    transform: scale(1.1); transform-origin: top left;
    overflow: hidden; background: var(--wood-main);
  }
  .status-bar {
    position: absolute; left: 0; top: 0; width: 566px; height: 42px;
    background: var(--status-bg); color: var(--status-fg);
    font-size: 17px; font-weight: 500;
  }
  .status-bar .carrier { position: absolute; left: 14px; top: 11px; display: flex; align-items: center; gap: 6px; }
  .status-bar .dots { letter-spacing: -1px; font-size: 14px; }
  .status-bar .time { position: absolute; left: 0; right: 0; top: 11px; text-align: center; font-weight: 600; }
  .status-bar .battery { position: absolute; right: 12px; top: 11px; display: flex; align-items: center; gap: 6px; }
  .battery-cell { width: 34px; height: 14px; background: #fff; border-radius: 3px; position: relative; }
  .battery-cell::after { content: ""; position: absolute; right: -4px; top: 4px; width: 2px; height: 6px; background: #fff; border-radius: 1px; }

  /* Main content behind the menu */
  .wood-header { position: absolute; left: 374px; top: 42px; width: 192px; height: 69px; background: var(--wood-top); }
  .wood-edge { position: absolute; left: 534px; top: 111px; width: 32px; height: 893px; background: var(--wood-edge); }
  .tile { position: absolute; top: 144px; height: 95px; background: var(--tile); border: 2px solid var(--tile-edge); }
  .tile-left { left: 374px; width: 32px; }
  .tile-score { left: 415px; width: 119px; text-align: center; }
  .tile-score .label { display: block; margin-top: 16px; font-size: 17px; color: var(--tile-label); }
  .tile-score .value { display: block; font-size: 38px; line-height: 40px; color: var(--score); font-weight: 400; }
  .card { position: absolute; left: 374px; width: 160px; background: var(--card); }
  .card-prompt { top: 261px; height: 127px; }
  .card-writing { top: 405px; height: 501px; }
  .card-writing .guide { position: absolute; left: 0; right: 0; top: 249px; height: 1px; background: var(--card-line); }
  .next-button {
    position: absolute; left: 386px; top: 921px; width: 148px; height: 56px;
    background: var(--next-bg); color: var(--next-text);
    font-size: 21px; font-weight: 500;
    display: flex; align-items: center; justify-content: center; gap: 20px;
  }

  /* Side menu */
  .side-menu { position: absolute; left: 0; top: 42px; width: 374px; height: 962px; background: var(--menu-bg); }
  .menu-toggle {
    position: absolute; left: 25px; top: 14px; width: 59px; height: 38px;
    background: var(--menu-btn); border: 1px solid var(--menu-btn-edge); border-radius: 2px;
    display: flex; align-items: center; justify-content: center;
  }
  .search-field {
    position: absolute; left: 26px; top: 75px; width: 319px; height: 45px;
    background: var(--search-bg); border-radius: 6px;
    display: flex; align-items: center; justify-content: space-between; padding: 0 14px 0 21px;
    font-size: 17px; color: var(--search-text);
  }
  .menu-list { position: absolute; left: 24px; top: 143px; width: 324px; list-style: none; border-top: 1px solid var(--menu-line); }
  .menu-list li {
    height: 52.5px; border-bottom: 1px solid var(--menu-line);
    display: flex; align-items: center; gap: 14px; padding-left: 6px;
    color: var(--menu-text); font-size: 17px;
  }
  .menu-list svg { width: 22px; height: 22px; flex: none; }
</style>
</head>
<body>
<div class="stage">
  <div class="screen">
    <div class="status-bar">
      <div class="carrier"><span class="dots">●●●●●</span><span>NOVA</span>
        <svg width="18" height="14" viewBox="0 0 18 14"><path d="M1 5a11 11 0 0 1 16 0M4 8a7 7 0 0 1 10 0M7 11a3 3 0 0 1 4 0" fill="none" stroke="#fff" stroke-width="2" stroke-linecap="round"/></svg>
      </div>
      <div class="time">4:21 PM</div>
      <div class="battery">
        <svg width="10" height="16" viewBox="0 0 10 16"><path d="M2 4l6 6-3 3V3l3 3-6 6" fill="none" stroke="#aaa" stroke-width="1.4"/></svg>
        <span>100%</span><span class="battery-cell"></span>
      </div>
    </div>

    <div class="wood-header"></div>
    <div class="wood-edge"></div>
    <div class="tile tile-left"></div>
    <div class="tile tile-score"><span class="label">Correct</span><span class="value">102</span></div>
    <div class="card card-prompt"></div>
    <div class="card card-writing" role="img" aria-label="Faint kana stroke guide for writing practice"><div class="guide"></div></div>
    <div class="next-button"><span>NEXT</span>
      <svg width="22" height="30" viewBox="0 0 22 30"><path d="M3 3l14 12L3 27" fill="none" stroke="#a86b3c" stroke-width="7" stroke-linejoin="round" stroke-linecap="round"/></svg>
    </div>

    <nav class="side-menu">
      <div class="menu-toggle">
        <svg width="28" height="24" viewBox="0 0 28 24" fill="#fff">
          <rect x="0" y="1" width="4" height="4"/><rect x="7" y="1" width="21" height="4"/>
          <rect x="0" y="10" width="4" height="4"/><rect x="7" y="10" width="21" height="4"/>
          <rect x="0" y="19" width="4" height="4"/><rect x="7" y="19" width="21" height="4"/>
        </svg>
      </div>
      <div class="search-field"><span>search</span>
        <svg width="26" height="26" viewBox="0 0 26 26"><circle cx="10" cy="10" r="8" fill="none" stroke="#555" stroke-width="2"/><path d="M16 16l8 8" stroke="#555" stroke-width="3" stroke-linecap="round"/></svg>
      </div>
      <ul class="menu-list">
        <li><svg viewBox="0 0 22 22"><circle cx="11" cy="11" r="7" fill="none" stroke="#fff" stroke-width="4" stroke-dasharray="3 2.5"/><circle cx="11" cy="11" r="5" fill="none" stroke="#fff" stroke-width="2.5"/></svg>Setting</li>
        <li><svg viewBox="0 0 22 22" fill="none" stroke="#fff" stroke-width="2" stroke-linecap="round"><path d="M3 6h10M8 2v14c0 3-4 4-4 1 0-3 6-6 10-4 4 2 2 8-2 8M15 4l3 2"/></svg>Reading Test</li>
        <li><svg viewBox="0 0 22 22" fill="#fff"><rect x="2" y="3" width="11" height="17"/><rect x="16" y="3" width="3" height="3"/><rect x="16" y="8" width="3" height="12"/></svg>Writting Test</li>
        <li><svg viewBox="0 0 22 22" fill="none" stroke="#fff" stroke-width="3" stroke-linecap="round"><path d="M3 5h12a4 4 0 0 1 0 8H9v7"/></svg>Game</li>
        <li><svg viewBox="0 0 22 22" fill="none" stroke="#fff" stroke-width="1.6"><rect x="3" y="2" width="13" height="17"/><path d="M6 6h7M6 9h7M6 12h5M14 19l5-6"/></svg>Paper Mode</li>
        <li><svg viewBox="0 0 22 22" fill="none" stroke="#fff" stroke-width="1.8"><rect x="2" y="2" width="18" height="18"/><path d="M7 6h7l-5 6M9 10l5 5M5 17h12"/></svg>Dictionary</li>
      </ul>
    </nav>
  </div>
</div>
</body>
</html>
```